Flyer für Unterstützung in der Personalarbeit
Zielgruppe
HR Freelancer, bitte Dienstleistung für Unternehmen an, die temporär Unterstützung in der Personalarbeit (Personalprozesse, Recruiting, Lohn- und Gehaltsabrechnung, HR Management, Administration) benötigen.
Aufgabenstellung
Ich benötige einen mehrseitigen Flyer, der mich und meine Arbeit kurz vorstellt. Außerdem soll es in einem Teil darum gehen, warum ein HR Freelancer eine gute Wahl ist. Der Flyer/die Broschüre soll an Unternehmen versendet werden.
Ich wünsche mir ein modernes minimalistisches und dennoch ansprechendes Design. Ich benötige die Datei am Ende auch im Word Format, da ich zukünftig Referenzen und weitere Auftraggeber ergänzen muss.
Ich füge zudem verschiedene Bilder bei, dabei müssen nicht alle berücksichtigt werden.

```html
<!DOCTYPE html>
<html lang="de">
<head>
<meta charset="utf-8">
<title>Lena Morvik – HR Freelancer Flyer</title>
<link rel="stylesheet" href="https://fonts.googleapis.com/css2?family=Poppins:wght@300;400;500;600;700&family=Fira+Sans+Extra+Condensed:wght@600&display=swap">
<style>
:root{
  --coral:#ee5a45;
  --ink:#2b2b2b;
  --text:#4a4a4a;
  --panel:#f1f1f1;
  --swoosh:#4a4a4a;
  --stage:#34312f;
  --white:#ffffff;
}
*{margin:0;padding:0;box-sizing:border-box}
html,body{width:1082px;height:1200px;overflow:hidden;background:var(--stage)}
body{font-family:'Poppins',sans-serif;color:var(--text);position:relative}
.page{position:absolute;width:408px;height:578px;background:var(--white);overflow:hidden}
.p1{left:124px;top:13px}.p2{left:550px;top:13px}
.p3{left:124px;top:609px}.p4{left:550px;top:609px}
.abs{position:absolute}
.photo{position:absolute;border-bottom-left-radius:34px}
.swoosh{position:absolute;left:0;top:508px;width:408px;height:70px;display:block}

.brand-name{font-weight:300;color:#555;font-size:30px;letter-spacing:.5px;text-align:center;line-height:1}
.brand-tag{font-weight:400;color:#444;font-size:13px;letter-spacing:.6px;text-align:center}

.headline{font-family:'Fira Sans Extra Condensed',sans-serif;font-weight:600;color:var(--coral);font-size:27px;line-height:27px;text-align:center;left:0;width:408px}

.section-title{color:var(--coral);font-weight:600;font-size:10.5px;line-height:1.15}
.rule{height:1px;background:var(--coral);margin-top:4px}
.copy{font-size:7.6px;line-height:9.6px;color:var(--text)}

.contact{left:0;top:233px;width:193px;height:136px;background:var(--coral);border-radius:0 14px 14px 0;padding:12px 0 0 33px;color:var(--white)}
.contact h3{font-size:16px;font-weight:600;margin-bottom:5px}
.contact li{list-style:none;display:flex;align-items:center;gap:7px;font-size:10.6px;font-weight:500;height:17.7px}
.contact svg{width:12px;height:12px;flex:none}

.dots{list-style:none}
.dots li{position:relative;padding-left:8px;font-size:7.6px;line-height:8.6px;margin-bottom:3.4px}
.dots li::before{content:"";position:absolute;left:0;top:3px;width:2.6px;height:2.6px;border-radius:50%;background:var(--coral)}
.dots b{display:block;color:var(--ink);font-weight:600;font-size:7.8px;line-height:9.4px}

.role{font-weight:600;color:var(--ink);font-size:9.6px;line-height:11px;margin-bottom:6px}
.sub{color:var(--coral);font-weight:500;font-size:7.8px;margin-bottom:2px}

.big-title{color:var(--coral);font-weight:700;font-size:16.5px;line-height:18px}
.h13{color:var(--coral);font-weight:700;font-size:12.5px;line-height:1.1}

.services{left:203px;top:0;width:205px;height:510px;background:var(--panel);border-bottom-left-radius:24px}
.service-list li{margin-bottom:10px;line-height:8.8px}

.nums{list-style:none;counter-reset:n}
.nums li{counter-increment:n;position:relative;padding-left:11px;font-size:7.6px;line-height:8.8px;margin-bottom:8.5px}
.nums li::before{content:counter(n) ".";position:absolute;left:0;top:0;font-weight:600;color:var(--ink);font-size:7.2px}
.nums b{display:block;color:var(--ink);font-weight:600;font-size:7.8px;line-height:9.6px}

.cta{left:31px;top:392px;width:345px;height:108px;background:var(--panel);border-radius:12px;text-align:center;padding:13px 20px 0}
.cta h4{color:var(--coral);font-weight:700;font-size:12.3px;line-height:14px;margin-bottom:8px}
.cta p{font-size:10px;line-height:12px;color:#3a3a3a}
</style>
</head>
<body>

<section class="page p1">
  <div class="abs" style="left:0;top:80px;width:225px">
    <p class="brand-name">lena morvik</p>
  </div>
  <div class="abs" style="left:0;top:121px;width:225px">
    <p class="brand-tag">HR Freelancer</p>
  </div>
  <div class="photo" role="img" aria-label="Porträtfoto der HR-Freelancerin an einer Uferpromenade vor Bürogebäuden" style="left:225px;top:0;width:183px;height:154px;background:linear-gradient(135deg,#cfd3d4 0%,#9ea49f 45%,#6f6a5f 100%)"></div>

  <h1 class="abs headline" style="top:166px">Ihre HR-Freelancerin für<br>maßgeschneiderte Lösungen</h1>

  <div class="abs contact">
    <h3>Kontakt:</h3>
    <ul>
      <li><svg viewBox="0 0 12 12"><circle cx="6" cy="6" r="5.4" fill="none" stroke="#fff" stroke-width="1"/><path d="M4.2 3.4l1 .1.4 1.2-.6.5c.3.7.8 1.2 1.5 1.5l.5-.6 1.2.4.1 1c-2.6.4-4.6-1.6-4.1-4.1z" fill="#fff"/></svg>0170 / 12 34 56 78</li>
      <li><svg viewBox="0 0 12 12"><circle cx="6" cy="6" r="5.4" fill="none" stroke="#fff" stroke-width="1"/><rect x="3.3" y="4" width="5.4" height="4" fill="none" stroke="#fff" stroke-width=".8"/><path d="M3.3 4l2.7 2.2L8.7 4" fill="none" stroke="#fff" stroke-width=".8"/></svg>mail@lenamorvik.de</li>
      <li><svg viewBox="0 0 12 12"><circle cx="6" cy="6" r="5.4" fill="#fff"/></svg>Lena Morvik</li>
      <li><svg viewBox="0 0 12 12"><path d="M6 11.5C3.8 8.6 2.7 6.6 2.7 4.9a3.3 3.3 0 016.6 0c0 1.7-1.1 3.7-3.3 6.6z" fill="#fff"/><circle cx="6" cy="4.9" r="1.3" fill="var(--coral)"/></svg>Waldfelde, Berlin</li>
      <li><svg viewBox="0 0 12 12"><circle cx="6" cy="6" r="5.4" fill="#fff"/><g fill="none" stroke="var(--coral)" stroke-width=".6"><circle cx="6" cy="6" r="3.2"/><ellipse cx="6" cy="6" rx="1.4" ry="3.2"/><path d="M2.8 6h6.4M3.3 4.4h5.4M3.3 7.6h5.4"/></g></svg>lenamorvik.de</li>
    </ul>
  </div>

  <div class="abs" style="left:220px;top:239px;width:161px">
    <h2 class="section-title">Über mich</h2>
    <div class="rule" style="width:147px"></div>
    <p class="copy" style="margin-top:6px">Ich bin eine HR-Generalistin mit über 10 Jahren Erfahrung. Als HR-Freelancerin helfe ich Unternehmen dabei, ihre HR-Prozesse zu optimieren und maßgeschneiderte Lösungen zu finden. Ob Personalbetreuung, Recruiting oder Prozessverbesserungen – ich kenne die Herausforderungen und packe sie mit Leidenschaft an.</p>
  </div>

  <div class="abs" style="left:220px;top:377px;width:161px">
    <h2 class="section-title">Berufliche Stationen und relevante Projekterfahrung</h2>
    <div class="rule" style="width:147px"></div>
    <p class="copy" style="margin-top:6px">Ich bin eine HR-Generalistin mit über 10 Jahren Erfahrung. Als HR-Freelancerin helfe ich Unternehmen dabei, ihre HR-Prozesse zu optimieren und maßgeschneiderte Lösungen zu finden. Ob Personalbetreuung, Recruiting oder Prozessverbesserungen – ich kenne die Herausforderungen und packe sie mit Leidenschaft an.</p>
  </div>

  <div class="abs" style="left:33px;top:382px;width:150px">
    <h2 class="section-title">Expertise</h2>
    <div class="rule" style="width:146px"></div>
    <ul class="dots" style="margin-top:7px">
      <li>HR Generalist / Personalbetreuung</li>
      <li>Full Life Cycle Recruiting</li>
      <li>Einführung und Betreuung von Bewerbermanagementsystemen</li>
      <li>Vorbereitende Lohn- und Gehaltsabrechnung (Paylix)</li>
      <li>Zusammenarbeit mit Arbeitnehmervertretungen</li>
      <li>Berufserfahrung in verschiedenen Dienstleistungsbranchen</li>
      <li>Fließende Englischkenntnisse</li>
    </ul>
  </div>

  <svg class="swoosh" viewBox="0 0 408 70" preserveAspectRatio="none" aria-hidden="true">
    <path d="M0 20 Q200 80 408 0 V70 H0Z" fill="var(--swoosh)"/>
    <path d="M0 36 Q200 86 408 20 V70 H0Z" fill="var(--white)"/>
    <path d="M0 46 Q200 92 408 32 V70 H0Z" fill="var(--coral)"/>
  </svg>
</section>

<section class="page p2">
  <div class="abs" style="left:29px;top:37px;width:175px">
    <h2 class="big-title">Berufliche Stationen und relevante Projekterfahrung</h2>
    <div class="rule" style="width:165px;margin-top:10px"></div>
  </div>
  <div class="photo" role="img" aria-label="Foto der HR-Freelancerin auf einer Treppe sitzend mit Smartphone" style="left:213px;top:0;width:195px;height:198px;background:linear-gradient(150deg,#d9d6d0 0%,#a9a39a 50%,#3f3c3a 100%)"></div>

  <div class="abs" style="left:32px;top:127px;width:170px">
    <p class="role">HR-Freelancerin (seit 2024):</p>
    <p class="sub">Interim HR Operations</p>
    <ul class="dots">
      <li>Betreuung eines Unternehmens mit ca. 10.000 Mitarbeitenden</li>
      <li>Bearbeitung von HR Operations Anfragen</li>
      <li>Beratung in übergreifenden HR Prozessen zu Disziplinarmaßnahmen, Bescheinigungswesen und Verträgen</li>
      <li>Administrative und organisatorische Beratung der Teamleitung</li>
      <li>Beratung hinsichtlich der vor- und nachbereitenden Payroll</li>
    </ul>
    <p class="sub" style="margin-top:6px">Senior HR Freelancer:</p>
    <ul class="dots">
      <li>Unterstützung eines Online-Marketing-Unternehmens mit ca. 200 Mitarbeitenden</li>
      <li>Beratung hinsichtlich operativer Personalthemen</li>
      <li>Optimierung des Onboardings und der Personalbetreuung</li>
    </ul>
  </div>

  <div class="abs" style="left:222px;top:223px;width:162px">
    <p class="role">Recruitment Manager bei Kleidwerk (2014 – 2018)</p>
    <ul class="dots">
      <li>Leitung des deutschlandweiten Recruitment-Teams</li>
      <li>Gesamtverantwortung für den Bewerbungsprozess: Stellenanzeigen, Auswahlgespräche</li>
      <li>Durchführung von High Volume Recruitings bei Neueröffnungen (ca. 300 Mitarbeitende)</li>
      <li>Unterstützung von Führungskräften bei der Rekrutierung und Teamaufbau</li>
    </ul>
  </div>

  <div class="abs" style="left:32px;top:373px;width:170px">
    <p class="role">HR-Generalistin bei Norvat Service Solutions (2018 – 2023)</p>
    <ul class="dots">
      <li>Personalbetreuung und -verwaltung von ca. 650 Mitarbeitenden</li>
      <li>Vorbereitung von Lohn- und Gehaltsabrechnungen (Paylix)</li>
      <li>Koordination von Personalvorgängen (Einstellungen, Vertragsänderungen, Austritte)</li>
      <li>Ansprechpartnerin für Mitarbeitende und Führungskräfte</li>
      <li>Durchführung des BEM-Prozesses zur Wiedereingliederung nach Krankheitszeiten</li>
    </ul>
  </div>

  <div class="abs" style="left:222px;top:373px;width:162px">
    <p class="role">HR Coordinator bei der TAVELO Hotelgruppe (2013 – 2014)</p>
    <ul class="dots">
      <li>Personaladministration und Bewerbermanagement</li>
      <li>Vorbereitende Lohnabrechnung und Unterstützung des externen Lohnbüros</li>
      <li>Pflege von Personalakten und Stammdaten</li>
      <li>Weiterentwicklung und Implementierung von HR-Prozessen</li>
    </ul>
  </div>

  <svg class="swoosh" viewBox="0 0 408 70" preserveAspectRatio="none" aria-hidden="true">
    <path d="M0 20 Q200 80 408 0 V70 H0Z" fill="var(--swoosh)"/>
    <path d="M0 36 Q200 86 408 20 V70 H0Z" fill="var(--white)"/>
    <path d="M0 46 Q200 92 408 32 V70 H0Z" fill="var(--coral)"/>
  </svg>
</section>

<section class="page p3">
  <div class="abs services"></div>

  <div class="abs" style="left:31px;top:30px;width:150px">
    <h2 class="h13">Was mich auszeichnet</h2>
    <div class="rule" style="width:147px;margin-top:7px"></div>
    <ul class="dots" style="margin-top:9px">
      <li style="margin-bottom:8px"><b>Kommunikativ &amp; Organisiert</b>Ich setze auf klare Kommunikation und strukturiertes Arbeiten.</li>
      <li style="margin-bottom:8px"><b>Empathisch &amp; Diskret</b>Der respektvolle Umgang mit Menschenist mir wichtig.</li>
      <li><b>Innovativ &amp; Teamfähig</b>Immer offen für neue Ideen und eine starke Teamplayerin.</li>
    </ul>
  </div>

  <div class="abs" role="img" aria-label="Foto einer Hand, die Holzwürfel mit HR-Symbolen zu einer Pyramide stapelt" style="left:0;top:178px;width:188px;height:218px;border-radius:0 18px 18px 0;background:linear-gradient(180deg,#b9dcd6 0%,#cfe6e2 55%,#e4dccd 100%)"></div>

  <div class="abs" style="left:31px;top:412px;width:160px">
    <h2 class="section-title">Rahmendaten</h2>
    <div class="rule" style="width:128px"></div>
    <ul class="dots" style="margin-top:7px">
      <li style="margin-bottom:6px"><b>Verfügbarkeit</b>Ab sofort, Teilzeit / Vollzeit, flexibel nach Absprache</li>
      <li><b>Einsatzort</b>Deutschlandweit remote, mit planbarer Reisetätigkeit. In Berlin/Brandenburg auch Hybrid möglich.</li>
    </ul>
  </div>

  <div class="abs" style="left:220px;top:31px;width:162px">
    <h2 class="h13">Leistungen im Überblick</h2>
    <div class="rule" style="width:152px;margin-top:7px"></div>
    <ul class="dots service-list" style="margin-top:11px">
      <li><b>Interim HR &amp; Projektmanagement</b>Temporäre Übernahme von HR-Aufgaben zur Überbrückung von Vakanzen, Unterstützung in Projekten oder bei Engpässen.</li>
      <li><b>Onboarding-Prozesse</b>Gestaltung und Optimierung von Onboarding-Prozessen zur schnellen und effektiven Integration neuer Mitarbeiter.</li>
      <li><b>Recruiting &amp; High Volume Recruiting</b>Rekrutierung der passenden Talente für Ihr Unternehmen, inklusive vollständigem Bewerbermanagement und Vorstellungsgesprächen.</li>
      <li><b>Vorbereitende Abrechnung &amp; Payroll</b>Unterstützung bei Lohn- und Gehaltsabrechnungen, einschließlich Pflege von Daten in Paylix und Zeiterfassungssystemen.</li>
      <li><b>Personalbetreuung &amp; Verwaltung</b>Umfassende Betreuung Ihrer Mitarbeiter und Sicherstellung reibungsloser Personalprozesse.</li>
      <li><b>Betriebliches Eingliederungsmanagement (BEM)</b>Begleitung und Koordination von BEM-Prozessen zur erfolgreichen Wiedereingliederung nach längeren Krankheitsphasen.</li>
      <li><b>Zusammenarbeit mit Arbeitnehmervertretungen</b>Unterstützung bei der Kommunikation und Verhandlungen mit Betriebsräten zu arbeitsrechtlichen Themen.</li>
      <li><b>Organisationsentwicklung &amp; Prozessverbesserung</b>Analyse und Optimierung von Prozessen zur Steigerung der Effizienz und Flexibilität Ihres Unternehmens.</li>
    </ul>
  </div>

  <svg class="swoosh" viewBox="0 0 408 70" preserveAspectRatio="none" aria-hidden="true">
    <path d="M0 20 Q200 80 408 0 V70 H0Z" fill="var(--swoosh)"/>
    <path d="M0 36 Q200 86 408 20 V70 H0Z" fill="var(--white)"/>
    <path d="M0 46 Q200 92 408 32 V70 H0Z" fill="var(--coral)"/>
  </svg>
</section>

<section class="page p4">
  <div class="abs" style="left:28px;top:30px;width:176px">
    <h2 class="h13">Warum ein HR-Freelancer?</h2>
    <div class="rule" style="width:173px;margin-top:7px"></div>
    <ul class="nums" style="margin-top:10px">
      <li><b>Flexibilität</b>Freelancer können stundenweise oder projektbezogen engagiert werden – man bezahlt nur für tatsächlich benötigte Leistungen.</li>
      <li><b>Spezialisierte Expertise</b>Sie bringen Fachwissen aus verschiedenen Branchen mit und bieten sofortige Lösungen für spezifische HR-Aufgaben.</li>
      <li><b>Kosteneffizienz</b>Keine Fixkosten für Sozialleistungen, nur flexible Bezahlung nach Aufwand.</li>
      <li><b>Unabhängige Perspektive</b>Externe Freelancer bringen frische Ideen und können Prozesse objektiv bewerten und optimieren.</li>
      <li><b>Schnelle Verfügbarkeit</b>Freelancer sind sofort einsatzbereit und unterstützen kurzfristig bei Engpässen oder Projekten.</li>
      <li><b>Projektbezogene Unterstützung</b>Sie übernehmen zeitlich begrenzte Aufgaben und Projekte, von der Planung bis zur Umsetzung.</li>
      <li><b>Netzwerk und Erfahrung</b>Durch Erfahrung in verschiedenen Unternehmen bieten sie wertvolle Kontakte und Best Practices.</li>
    </ul>
  </div>

  <div class="photo" role="img" aria-label="Porträtfoto der HR-Freelancerin im dunklen Blazer an einer hellen Wand" style="left:226px;top:0;width:182px;height:237px;background:linear-gradient(160deg,#e6e4df 0%,#c9c5be 45%,#2f2d2c 100%)"></div>

  <div class="abs" style="left:208px;top:306px;width:182px">
    <p class="brand-name" style="font-size:27px">lena morvik</p>
  </div>
  <div class="abs" style="left:208px;top:346px;width:182px">
    <p class="brand-tag">HR Freelancer</p>
  </div>

  <div class="abs cta">
    <h4>Lassen Sie uns Ihre HR-Themen gemeinsam erfolgreich gestalten!</h4>
    <p>Kontaktieren Sie mich gerne für ein unverbindliches Gespräch – ich freue mich darauf, Ihre HR-Prozesse zu optimieren und Ihr Team erfolgreich zu unterstützen.</p>
  </div>

  <svg class="swoosh" viewBox="0 0 408 70" preserveAspectRatio="none" aria-hidden="true">
    <path d="M0 20 Q200 80 408 0 V70 H0Z" fill="var(--swoosh)"/>
    <path d="M0 36 Q200 86 408 20 V70 H0Z" fill="var(--white)"/>
    <path d="M0 46 Q200 92 408 32 V70 H0Z" fill="var(--coral)"/>
  </svg>
</section>

</body>
</html>
```